Website design for staffing/workforce solutions company - Harbor Crest Solutions

Create a launch-ready website
Harbor Crest Solutions also known as HCS. This is a company that specializes in Staffing/Work force solutions for Healthcare/IT/Logistics/Maintenance/Construction/Manufacturing/Industrial/General Labor. HCS works with government agencies/contracts also. Use the attached logo in the build of the website. Website should be clean, modern, engaging, innovative. Website needs to speak to the professional services industry.
Harbor Crest Solutions or HCS is a certified VOSB, SDVOSB, DBE and Minority-Owned Business.
The website needs to be compliant for government contracting.

Website needs to include the following--
Modern UI/UX Enhancements: A hero section with a strong call-to-action.
Government Contracting Compliance: Certification display and a Capability Statement download.
Advanced Careers Section: A dedicated job application portal.
Social Media & Lead Generation: Links to Workvine, Quillo, and Pagebloom.
Security & Performance: Optimized for SEO, fast loading, and mobile responsiveness.
1. Modern Design Upgrades
๐Ÿ”น Upgrade UI/UX for a Professional, Trustworthy Look
โœ… Full-width hero banner with a high-quality background image representing business, technology, and workforce solutions.
โœ… Animated elements (subtle transitions for smooth browsing experience).
โœ… Bold CTA buttons for easy navigation to key actions (e.g., โ€œGet Startedโ€ or โ€œRequest a Consultationโ€).
โœ… Dark-themed header with contrasting colors (professional & government-trustworthy).
โœ… New Homepage Hero Section Example:
"Your Trusted Partner in Workforce, IT, Maintenance & Logistics Solutions"
Button: "Discover Our Services"

2. Enhanced Government Contracting Section (Key for Compliance)
๐Ÿ“Œ Essential for securing contracts & building credibility
โœ… Capability Statement (Downloadable PDF)

Showcase key past contracts, company qualifications, and services in a downloadable format for government buyers.
โœ… Certifications Display (VOSB, SDVOSB, DBE, Minority-Owned Business)

Visual badge display to emphasize legitimacy for government contracts.
โœ… Procurement Readiness Details

NAICS Codes, DUNS Number, CAGE Code, and relevant KPR.example registration details.
โœ… Past Performance Showcase (Case Studies Section)

Highlight successful projects and government contracts.
โœ… Compliance & Security

Add SOC 2, HIPAA (for healthcare staffing), and ITAR compliance if applicable.
3. Advanced Job Search & Candidate Portal (For Staffing Services)
๐Ÿ“Œ To attract top talent for staffing contracts

โœ… Advanced Job Search Feature

Filters: Industry, location, job type (contract/full-time), salary range, and clearance level (for government jobs).
โœ… Candidate Login Portal

Applicants can upload resumes, track applications, and receive job alerts.
โœ… Employer Portal (For Businesses Hiring Through HCS)

A dedicated section for companies to submit staffing requests and view candidate matches.
4. Service-Specific Landing Pages (SEO & Engagement)
๐Ÿ“Œ Helps different industries find relevant services faster

๐Ÿ”น Dedicated Pages for Each Service:
โœ… Staffing & Workforce Solutions

Specialized sections for Healthcare, IT, Construction, Industrial, and General Labor staffing.
โœ… IT Services

List services like Cybersecurity, Cloud Solutions, and IT Consulting.
Showcase tech stack & certifications.
โœ… Logistics & Maintenance

Detail fleet management, supply chain services, and industrial maintenance.
โœ… Government Contracting Solutions

A streamlined page for government agencies.
5. Security & Compliance Upgrades (For Government Work)
๐Ÿ“Œ To ensure compliance & credibility in government contracting

โœ… SSL Certification (100% Required for Security)

Secure client and job applicant data.
โœ… ADA Compliance (Accessibility)

Ensure the website follows WCAG 2.1 accessibility standards for government clients.
โœ… GDPR & Data Protection Features

A privacy policy and terms of service to comply with data regulations.
6. Performance & Mobile Optimization
๐Ÿ“Œ To ensure fast loading & responsiveness

โœ… Mobile-Responsive Design

Optimized for mobile-friendly navigation since many users browse from phones.
โœ… Fast-Loading Pages

Optimize images & implement lazy loading for better site speed.
โœ… SEO-Optimized Pages

Improve search ranking on Findoro with:
Keyword-optimized content (e.g., โ€œGovernment Contracting Staffing Servicesโ€)
Schema markup for job listings
Blog/articles about staffing trends
7. Social Media & Lead Generation
๐Ÿ“Œ For brand credibility & client engagement

โœ… Workvine, Quillo, Pagebloom Integration

Display recent updates from Workvine (primary for B2B & government).
โœ… Lead Capture Forms

Forms for business inquiries, talent applications, and government RFPs.
โœ… Client & Candidate Testimonials
Showcase client success stories & employee experiences

Good websites to pull examples for inspiration/direction--
https://www.vlmn.example/
https://www.torvana.example/
https://brightmeridian.example/homepage/
https://www.valdorcheck.example/capability-statement

Industry/Entity Type

Staffing/Professional Services

Coding

Coded - Design and coding required

Number of Pages Required

5+ page

Requirements
Must have
• Website needs to include the following-- Modern UI/UX Enhancements: A hero section with a strong call-to-action. Government Contracting Compliance: Certification display and a Capability Statement download. Advanced Careers Section: A dedicated job application portal. Social Media & Lead Generation: Links to Workvine, Quillo, and Pagebloom. Security & Performance: Optimized for SEO, fast loading, and mobile responsiveness. 1. Modern Design Upgrades ๐Ÿ”น Upgrade UI/UX for a Professional, Trustworthy Look โœ… Full-width hero banner with a high-quality background image representing business, technology, and workforce solutions. โœ… Animated elements (subtle transitions for smooth browsing experience). โœ… Bold CTA buttons for easy navigation to key actions (e.g., โ€œGet Startedโ€ or โ€œRequest a Consultationโ€). โœ… Dark-themed header with contrasting colors (professional & government-trustworthy). โœ… New Homepage Hero Section Example: "Your Trusted Partner in Workforce, IT, & Logistics Solutions" Button: "Discover Our Services" 2. Enhanced Government Contracting Section (Key for Compliance) ๐Ÿ“Œ Essential for securing contracts & building credibility โœ… Capability Statement (Downloadable PDF) Showcase key past contracts, company qualifications, and services in a downloadable format for government buyers. โœ… Certifications Display (VOSB, SDVOSB, DBE, Minority-Owned Business) Visual badge display to emphasize legitimacy for government contracts. โœ… Procurement Readiness Details NAICS Codes, DUNS Number, CAGE Code, and relevant KPR.example registration details. โœ… Past Performance Showcase (Case Studies Section) Highlight successful projects and government contracts. โœ… Compliance & Security Add SOC 2, HIPAA (for healthcare staffing), and ITAR compliance if applicable. 3. Advanced Job Search & Candidate Portal (For Staffing Services) ๐Ÿ“Œ To attract top talent for staffing contracts โœ… Advanced Job Search Feature Filters: Industry, location, job type (contract/full-time), salary range, and clearance level (for government jobs). โœ… Candidate Login Portal Applicants can upload resumes, track applications, and receive job alerts. โœ… Employer Portal (For Businesses Hiring Through HCS) A dedicated section for companies to submit staffing requests and view candidate matches. 4. Service-Specific Landing Pages (SEO & Engagement) ๐Ÿ“Œ Helps different industries find relevant services faster ๐Ÿ”น Dedicated Pages for Each Service: โœ… Staffing & Workforce Solutions Specialized sections for Healthcare, IT, Construction, Industrial, and General Labor staffing. โœ… IT Services List services like Cybersecurity, Cloud Solutions, and IT Consulting. Showcase tech stack & certifications. โœ… Logistics & Maintenance Detail fleet management, supply chain services, and industrial maintenance. โœ… Government Contracting Solutions A streamlined page for government agencies. 5. Security & Compliance Upgrades (For Government Work) ๐Ÿ“Œ To ensure compliance & credibility in government contracting โœ… SSL Certification (100% Required for Security) Secure client and job applicant data. โœ… ADA Compliance (Accessibility) Ensure the website follows WCAG 2.1 accessibility standards for government clients. โœ… GDPR & Data Protection Features A privacy policy and terms of service to comply with data regulations. 6. Performance & Mobile Optimization ๐Ÿ“Œ To ensure fast loading & responsiveness โœ… Mobile-Responsive Design Optimized for mobile-friendly navigation since many users browse from phones. โœ… Fast-Loading Pages Optimize images & implement lazy loading for better site speed. โœ… SEO-Optimized Pages Improve search ranking on Findoro with: Keyword-optimized content (e.g., โ€œGovernment Contracting Staffing Servicesโ€) Schema markup for job listings Blog/articles about staffing trends 7. Social Media & Lead Generation ๐Ÿ“Œ For brand credibility & client engagement โœ… Workvine, Quillo, Pagebloom Integration Display recent updates from Workvine (primary for B2B & government). โœ… Lead Capture Forms Forms for business inquiries, talent applications, and government RFPs. โœ… Client & Candidate Testimonials Showcase client success stories & employee experiences Good websites to pull examples for inspiration/direction-- https://www.vlmn.example/ https://www.torvana.example/ https://brightmeridian.example/homepage/

```html
<!DOCTYPE html>
<html lang="en">
<head>
<meta charset="utf-8">
<title>Harbor Crest Solutions — Workforce, IT &amp; Logistics</title>
<link href="https://fonts.googleapis.com/css2?family=Cabin:wght@400;500;600;700&display=swap" rel="stylesheet">
<style>
:root{
  --canvas:#e9e9ec;
  --ink:#1a1a1a;
  --header:#1f1f1f;
  --footer:#1c1c1c;
  --red:#c8141b;
  --red-dark:#a80f15;
  --navy:#0b1457;
  --navy-deep:#081048;
  --strip:#ececec;
  --gray:#d9d9d9;
  --white:#ffffff;
  --muted:#c9cbe0;
  --tick:#2f8fea;
}
*{box-sizing:border-box;margin:0;padding:0}
html,body{width:1200px;height:1200px;overflow:hidden;background:var(--canvas);font-family:"Cabin",sans-serif;color:var(--ink)}
.stage{position:relative;width:1200px;height:1200px;overflow:hidden}
.page{position:absolute;left:341px;top:10px;width:718px;height:1640px;transform:scale(0.72);transform-origin:0 0;background:var(--white);overflow:hidden}
.abs{position:absolute}

/* header */
.site-header{left:0;top:0;width:718px;height:40px;background:var(--header)}
.brand{position:absolute;left:94px;top:12px;color:var(--red);font-weight:600;font-size:12px;letter-spacing:1px;display:flex;align-items:center;gap:5px}
.brand-mark{width:9px;height:9px;border:1.5px solid var(--red)}
.nav{position:absolute;left:318px;top:14px;display:flex;gap:20px;font-size:9.5px;color:var(--white)}
.menu-icon{position:absolute;left:608px;top:16px}

/* hero */
.hero{left:0;top:40px;width:718px;height:316px}
.hero-photo-left{position:absolute;left:0;top:0;width:206px;height:316px;background:linear-gradient(135deg,#8a7a5a 0%,#c9a24a 30%,#5b4a3c 60%,#9a958e 100%)}
.hero-photo-right{position:absolute;left:511px;top:0;width:207px;height:316px;background:linear-gradient(160deg,#cfccc6 0%,#a9a49c 45%,#7d746c 100%)}
.hero-panel{position:absolute;left:206px;top:0;width:305px;height:335px;background:linear-gradient(180deg,rgba(200,20,27,.93),rgba(190,16,24,.97));border-radius:0 0 14px 14px;color:var(--white);z-index:2}
.hero-kicker{position:absolute;left:26px;top:98px;font-size:21px;font-weight:400;line-height:1.2}
.hero-title{position:absolute;left:26px;top:124px;font-size:23px;font-weight:700;line-height:1.25;width:270px}
.hero-copy{position:absolute;left:26px;top:188px;width:258px;font-size:7.6px;line-height:1.35}
.btn{display:flex;align-items:center;justify-content:center;font-weight:700;color:var(--white);border-radius:2px}
.btn-navy{position:absolute;left:105px;top:232px;width:100px;height:18px;background:var(--navy);font-size:7px}
.btn-red{position:absolute;left:105px;top:259px;width:100px;height:23px;background:var(--red-dark);font-size:8.5px;box-shadow:0 1px 0 rgba(0,0,0,.25)}
.hero-social{position:absolute;left:0;top:314px;width:305px;display:flex;justify-content:center;gap:10px;font-size:4.5px;line-height:1.1}
.chip{display:flex;align-items:center;gap:3px}
.chip i{width:9px;height:9px;border-radius:50%;background:#1d1d1d;display:block}

/* badges */
.badges{left:0;top:356px;width:718px;height:54px;background:var(--strip)}
.badge{position:absolute;top:26px;height:16px;background:#c7cbd6;border-radius:2px}

/* gov section */
.gov{left:0;top:410px;width:718px;height:222px;background:var(--navy);color:var(--white)}
.gov h2{position:absolute;left:94px;top:8px;font-size:15px;font-weight:600}
.gov-copy{position:absolute;left:94px;top:37px;width:258px;font-size:7px;line-height:1.3;color:#e4e6f3}
.ticks{position:absolute;left:94px;top:93px;list-style:none;font-size:7.3px;color:#dfe2f2}
.ticks li{display:flex;align-items:center;gap:11px;height:21.5px}
.gov-photo{position:absolute;left:380px;top:7px;width:298px;height:183px;background:linear-gradient(135deg,#6c6f6a 0%,#c9c8c2 40%,#eeeeea 65%,#8d9183 100%)}

/* contracts */
.contracts{left:0;top:632px;width:718px;height:262px;background:var(--white)}
.section-title{position:absolute;left:0;width:718px;text-align:center;font-size:15px;font-weight:600;color:var(--ink)}
.contract{position:absolute;width:95px;font-size:6px;line-height:1.25}
.contract b{display:block;font-weight:600;margin:5px 0 3px}
.contract span{display:block;font-size:4.6px;color:#444}
.view-all{position:absolute;left:498px;top:135px;width:125px;height:70px;background:var(--red);border-radius:4px;color:var(--white);font-size:8.5px;display:flex;align-items:center;justify-content:center;gap:8px}

/* recruitment */
.recruit{left:0;top:894px;width:718px;height:518px;background:var(--gray)}
.recruit-sub{position:absolute;left:0;top:37px;width:718px;text-align:center;font-size:7.3px;line-height:1.25;color:#333}
.card{position:absolute;width:169px;height:191px;background:var(--white);border-radius:2px;text-align:center}
.card svg{position:absolute;left:65px;top:44px}
.card h3{position:absolute;left:0;top:98px;width:100%;font-size:11px;font-weight:500}
.card p{position:absolute;left:0;top:115px;width:100%;font-size:8px;line-height:1.3;color:#333}
.card .btn-small{position:absolute;left:50px;top:156px;width:70px;height:11px;background:var(--red);color:var(--white);font-size:5.5px;border-radius:2px;display:flex;align-items:center;justify-content:center}
.card-brand{background:var(--navy-deep);display:flex;align-items:center;justify-content:center}
.card-brand span{color:var(--red);font-size:18px;font-weight:600;letter-spacing:1.5px}

/* footer */
.site-footer{left:0;top:1412px;width:718px;height:228px;background:var(--footer);color:#d6d6d6}
.footer-brand{position:absolute;left:104px;top:24px;font-size:12px;font-weight:600;color:var(--white);letter-spacing:1px;display:flex;align-items:center;gap:5px}
.footer-brand i{width:9px;height:9px;border:1.5px solid var(--white);display:block}
.fcol{position:absolute;top:36px;list-style:none;font-size:5.6px}
.fcol li{height:15px}
.fcol li.head{font-weight:700;color:var(--white);height:23px}
.soc{display:flex;align-items:center;gap:4px}
.soc i{width:5px;height:5px;border-radius:50%;border:1px solid #d6d6d6;display:block}
.footer-rule{position:absolute;left:104px;top:194px;width:508px;height:1px;background:#444}
.footer-legal{position:absolute;right:106px;top:208px;font-size:4.8px;display:flex;gap:8px}
</style>
</head>
<body>
<div class="stage">
<main class="page">

  <header class="site-header abs">
    <div class="brand"><span class="brand-mark"></span>HARBOR CREST</div>
    <nav class="nav"><span>Home</span><span>Recourses</span><span>Reviews</span><span>FAQ s</span><span>Contact</span></nav>
    <svg class="menu-icon" width="11" height="9" viewBox="0 0 11 9"><g fill="#c8141b"><rect x="0" y="0" width="2" height="2"/><rect x="3" y="0" width="8" height="2"/><rect x="0" y="3.5" width="2" height="2"/><rect x="3" y="3.5" width="8" height="2"/><rect x="0" y="7" width="2" height="2"/><rect x="3" y="7" width="8" height="2"/></g></svg>
  </header>

  <section class="hero abs">
    <div class="hero-photo-left" role="img" aria-label="Photo of a team collaborating in a bright office"></div>
    <div class="hero-photo-right" role="img" aria-label="Photo of a confident professional with arms crossed in an office"></div>
    <div class="hero-panel">
      <p class="hero-kicker">Your trusted Partner in</p>
      <h1 class="hero-title">Workforce, IT &amp; Logestic Solution</h1>
      <p class="hero-copy">We are an international staffing and professional services company dedicated to the belief that good people should be easy to find. Whether you need talent or transformation, let's grow together.</p>
      <a class="btn btn-navy">Discover Our Services</a>
      <a class="btn btn-red">Find a Job</a>
      <div class="hero-social">
        <span class="chip"><i></i>www.work<br>vine.com</span>
        <span class="chip"><i></i>www.page<br>bloom.com</span>
        <span class="chip"><i></i>www.snap<br>via.com</span>
        <span class="chip"><i></i>www.quil<br>lo.com</span>
      </div>
    </div>
  </section>

  <section class="badges abs" aria-label="Certifications and memberships">
    <span class="badge" style="left:94px;width:38px"></span>
    <span class="badge" style="left:176px;width:58px"></span>
    <span class="badge" style="left:278px;width:56px"></span>
    <span class="badge" style="left:378px;width:36px;background:#b9a56a"></span>
    <span class="badge" style="left:460px;width:56px"></span>
    <span class="badge" style="left:562px;width:28px"></span>
  </section>

  <section class="gov abs">
    <h2>with Precision &amp; Performance</h2>
    <p class="gov-copy">Unlock smarter, faster, and fully compliant contracting solutions tailored for federal, state, and local agencies.<br>Whether you're sourcing critical services, streamlining procurement, or navigating compliance, we're your trusted partner in driving government success.</p>
    <ul class="ticks">
      <li><svg width="11" height="11" viewBox="0 0 12 12"><circle cx="6" cy="6" r="6" fill="#2f8fea"/><path d="M3.3 6.2l1.8 1.8 3.6-3.8" stroke="#fff" stroke-width="1.4" fill="none"/></svg>Fast, Compliant Procurement Support</li>
      <li><svg width="11" height="11" viewBox="0 0 12 12"><circle cx="6" cy="6" r="6" fill="#2f8fea"/><path d="M3.3 6.2l1.8 1.8 3.6-3.8" stroke="#fff" stroke-width="1.4" fill="none"/></svg>Registered &amp; Certified Vendor</li>
      <li><svg width="11" height="11" viewBox="0 0 12 12"><circle cx="6" cy="6" r="6" fill="#2f8fea"/><path d="M3.3 6.2l1.8 1.8 3.6-3.8" stroke="#fff" stroke-width="1.4" fill="none"/></svg>Tailored Solutions for Federal, State &amp; Local Agencies</li>
      <li><svg width="11" height="11" viewBox="0 0 12 12"><circle cx="6" cy="6" r="6" fill="#2f8fea"/><path d="M3.3 6.2l1.8 1.8 3.6-3.8" stroke="#fff" stroke-width="1.4" fill="none"/></svg>Deep Regulatory Knowledge</li>
      <li><svg width="11" height="11" viewBox="0 0 12 12"><circle cx="6" cy="6" r="6" fill="#2f8fea"/><path d="M3.3 6.2l1.8 1.8 3.6-3.8" stroke="#fff" stroke-width="1.4" fill="none"/></svg>Streamlined Contract Management</li>
    </ul>
    <div class="gov-photo" role="img" aria-label="Photo of a smiling professional working on a laptop"></div>
  </section>

  <section class="contracts abs">
    <h2 class="section-title" style="top:16px">Past Contracts</h2>
    <div class="contract" style="left:100px;top:62px"><svg width="16" height="12" viewBox="0 0 16 12"><path d="M0 1h6l1.5 1.5H15V11H0z" fill="#1a1a1a"/><path d="M1.5 4.5H16L14.5 11H0z" fill="#333"/></svg><b>Streamlined Contract Management</b><span>Streamlined Contract Management</span><span>Streamlined Contract Management</span></div>
    <div class="contract" style="left:229px;top:62px"><svg width="16" height="12" viewBox="0 0 16 12"><path d="M0 1h6l1.5 1.5H15V11H0z" fill="#1a1a1a"/><path d="M1.5 4.5H16L14.5 11H0z" fill="#333"/></svg><b>Streamlined Contract Management</b><span>Streamlined Contract Management</span><span>Streamlined Contract Management</span></div>
    <div class="contract" style="left:364px;top:62px"><svg width="16" height="12" viewBox="0 0 16 12"><path d="M0 1h6l1.5 1.5H15V11H0z" fill="#1a1a1a"/><path d="M1.5 4.5H16L14.5 11H0z" fill="#333"/></svg><b>Streamlined Contract Management</b><span>Streamlined Contract Management</span><span>Streamlined Contract Management</span></div>
    <div class="contract" style="left:498px;top:62px"><svg width="16" height="12" viewBox="0 0 16 12"><path d="M0 1h6l1.5 1.5H15V11H0z" fill="#1a1a1a"/><path d="M1.5 4.5H16L14.5 11H0z" fill="#333"/></svg><b>Streamlined Contract Management</b><span>Streamlined Contract Management</span><span>Streamlined Contract Management</span></div>
    <div class="contract" style="left:100px;top:146px"><svg width="16" height="12" viewBox="0 0 16 12"><path d="M0 1h6l1.5 1.5H15V11H0z" fill="#1a1a1a"/><path d="M1.5 4.5H16L14.5 11H0z" fill="#333"/></svg><b>Streamlined Contract Management</b><span>Streamlined Contract Management</span><span>Streamlined Contract Management</span></div>
    <div class="contract" style="left:229px;top:146px"><svg width="16" height="12" viewBox="0 0 16 12"><path d="M0 1h6l1.5 1.5H15V11H0z" fill="#1a1a1a"/><path d="M1.5 4.5H16L14.5 11H0z" fill="#333"/></svg><b>Streamlined Contract Management</b><span>Streamlined Contract Management</span><span>Streamlined Contract Management</span></div>
    <div class="contract" style="left:364px;top:146px"><svg width="16" height="12" viewBox="0 0 16 12"><path d="M0 1h6l1.5 1.5H15V11H0z" fill="#1a1a1a"/><path d="M1.5 4.5H16L14.5 11H0z" fill="#333"/></svg><b>Streamlined Contract Management</b><span>Streamlined Contract Management</span><span>Streamlined Contract Management</span></div>
    <a class="view-all">View All <svg width="34" height="4" viewBox="0 0 34 4"><path d="M0 2h32" stroke="#fff" stroke-width=".8"/><path d="M31 0l3 2-3 2z" fill="#fff"/></svg></a>
  </section>

  <section class="recruit abs">
    <h2 class="section-title" style="top:12px">Recruitment Solutions</h2>
    <p class="recruit-sub">Unlock your business potential with our dedicated recruitment solutions.<br>Learn more about our full catalog of offerings for organizations of any size<br>across any industry.</p>

    <article class="card" style="left:95px;top:80px">
      <svg width="40" height="40" viewBox="0 0 40 40"><circle cx="20" cy="20" r="18" fill="none" stroke="#1a1a1a" stroke-width="2"/><circle cx="20" cy="20" r="13" fill="none" stroke="#1a1a1a" stroke-width="1.4"/><path d="M20 11v9l6 4" stroke="#1a1a1a" stroke-width="1.6" fill="none"/></svg>
      <h3>Flexible Placement</h3><p>Streamlined Contract Management<br>Streamlined Contract Management</p><a class="btn-small">Find a Job</a>
    </article>
    <article class="card card-brand" style="left:274px;top:80px"><span>HARBOR CREST</span></article>
    <article class="card" style="left:454px;top:80px">
      <svg width="40" height="40" viewBox="0 0 40 40"><circle cx="20" cy="20" r="18" fill="none" stroke="#1a1a1a" stroke-width="2"/><circle cx="20" cy="20" r="13" fill="none" stroke="#1a1a1a" stroke-width="1.4"/><path d="M20 11v9l6 4" stroke="#1a1a1a" stroke-width="1.6" fill="none"/></svg>
      <h3>Permanent Recruitment</h3><p>Streamlined Contract Management<br>Streamlined Contract Management</p><a class="btn-small">Find a Job</a>
    </article>
    <article class="card" style="left:95px;top:279px">
      <svg width="40" height="40" viewBox="0 0 40 40"><circle cx="20" cy="20" r="18" fill="none" stroke="#1a1a1a" stroke-width="2"/><circle cx="20" cy="20" r="13" fill="none" stroke="#1a1a1a" stroke-width="1.4"/><path d="M20 11v9l6 4" stroke="#1a1a1a" stroke-width="1.6" fill="none"/></svg>
      <h3>Diversity &amp; Inclusion</h3><p>Streamlined Contract Management<br>Streamlined Contract Management</p><a class="btn-small">Find a Job</a>
    </article>
    <article class="card" style="left:274px;top:279px">
      <svg width="40" height="40" viewBox="0 0 40 40"><circle cx="20" cy="20" r="18" fill="none" stroke="#1a1a1a" stroke-width="2"/><circle cx="20" cy="20" r="13" fill="none" stroke="#1a1a1a" stroke-width="1.4"/><path d="M20 11v9l6 4" stroke="#1a1a1a" stroke-width="1.6" fill="none"/></svg>
      <h3>Training</h3><p>Streamlined Contract Management<br>Streamlined Contract Management</p><a class="btn-small">Find a Job</a>
    </article>
    <article class="card" style="left:454px;top:279px">
      <svg width="40" height="40" viewBox="0 0 40 40"><circle cx="20" cy="20" r="18" fill="none" stroke="#1a1a1a" stroke-width="2"/><circle cx="20" cy="20" r="13" fill="none" stroke="#1a1a1a" stroke-width="1.4"/><path d="M20 11v9l6 4" stroke="#1a1a1a" stroke-width="1.6" fill="none"/></svg>
      <h3>Outsourcing</h3><p>Streamlined Contract Management<br>Streamlined Contract Management</p><a class="btn-small">Find a Job</a>
    </article>
  </section>

  <footer class="site-footer abs">
    <div class="footer-brand"><i></i>HARBOR CREST</div>
    <ul class="fcol" style="left:253px"><li class="head">Built For Creatives</li><li>Try Folionest Pro</li><li>Find Inspiration</li><li>Get Hired</li><li>Sell Creative Assets</li><li>Sell Freelance Services</li></ul>
    <ul class="fcol" style="left:348px"><li class="head">Find Talent</li><li>Post a Job</li><li>Graphic Designers</li><li>Photographers</li><li>Video Editors</li><li>Web Designers</li><li>Illustrators</li></ul>
    <ul class="fcol" style="left:442px"><li class="head">Folionest</li><li>About Folionest</li><li>Canvaro Portfolio</li><li>Download the App</li><li>Blog</li><li>Careers</li><li>Help Center</li><li>Contact Us</li></ul>
    <ul class="fcol" style="left:537px"><li class="head">Social</li><li class="soc"><i></i>Snapvia</li><li class="soc"><i></i>Quillo</li><li class="soc"><i></i>Pinlore</li><li class="soc"><i></i>Pagebloom</li><li class="soc"><i></i>Workvine</li></ul>
    <div class="footer-rule"></div>
    <div class="footer-legal"><span>English ▾</span><span>TOU</span><span>Privacy</span><span>Community</span><span>Cookie preferences</span><span>Do not sell or share my personal information</span></div>
  </footer>

</main>
</div>
</body>
</html>
```